Business Card *

A business card design
Use the logo uploaded in the brief page.
You may use placeholders in your design layouts.
I will provide the actual business card details to the winning designer.

Logo
Place for contact info (name, title, phone, email, etc)

Requirements
Must have
• Logo

```html
<!DOCTYPE html>
<html lang="en">
<head>
<meta charset="utf-8">
<title>Ridgefield Agriculture and Industry – Business Card</title>
<link href="https://fonts.googleapis.com/css2?family=Roboto:wght@400;500;700;900&display=swap" rel="stylesheet">
<style>
  :root {
    --backdrop: #3b3b3b;
    --card: #262626;
    --green: #2eb135;
    --grey: #a9a9a9;
    --white: #f2f2f2;
    --muted: #d6d6d6;
  }
  * { box-sizing: border-box; margin: 0; padding: 0; }
  html, body { width: 799px; height: 1200px; overflow: hidden; }
  body {
    background: var(--backdrop);
    font-family: "Roboto", Arial, sans-serif;
    position: relative;
  }
  .card {
    position: absolute;
    left: 60px;
    width: 680px;
    height: 388px;
    background: var(--card);
    border-radius: 6px;
    overflow: hidden;
    box-shadow: 0 8px 24px rgba(0,0,0,.35);
  }
  .card--front { top: 140px; }
  .card--back { top: 672px; }

  .brand {
    position: absolute;
    display: flex;
    align-items: center;
    gap: 14px;
  }
  .brand__dot {
    border-radius: 50%;
    background: var(--green);
    flex: none;
  }
  .brand__name {
    color: var(--grey);
    font-weight: 900;
    text-transform: uppercase;
    line-height: 1.05;
  }
  .card--front .brand {
    left: 50%; top: 50%;
    transform: translate(-50%, -50%);
  }
  .card--front .brand__dot { width: 64px; height: 64px; }
  .card--front .brand__name { font-size: 38px; }
  .card--front .brand__name small { display: block; font-size: 18px; letter-spacing: 2px; }

  .card--back .brand { right: 40px; top: 110px; gap: 10px; }
  .card--back .brand__dot { width: 40px; height: 40px; }
  .card--back .brand__name { font-size: 26px; }
  .card--back .brand__name small { display: block; font-size: 12px; letter-spacing: 1.5px; }

  .person { position: absolute; left: 34px; top: 32px; }
  .person__name { color: var(--green); font-weight: 900; font-size: 24px; text-transform: uppercase; letter-spacing: .5px; }
  .person__title { color: var(--muted); font-size: 13px; margin-top: 2px; }

  .contacts { position: absolute; left: 34px; top: 190px; list-style: none; }
  .contacts li { display: flex; align-items: center; gap: 12px; color: var(--white); font-size: 15px; height: 22px; }
  .contacts svg { width: 13px; height: 13px; fill: var(--green); flex: none; }

  .address {
    position: absolute; right: 40px; top: 230px;
    color: var(--white); font-size: 16px; text-align: right; line-height: 1.45;
  }
  .bands { position: absolute; left: 0; bottom: 0; width: 680px; height: 70px; }
  .tab-label {
    position: absolute; right: 36px; bottom: 14px;
    color: #fff; font-weight: 700; font-size: 17px;
  }
</style>
</head>
<body>

<section class="card card--front" aria-label="Card front">
  <div class="brand">
    <span class="brand__dot"></span>
    <p class="brand__name">Ridgefield<small>Agriculture and Industry</small></p>
  </div>
</section>

<section class="card card--back" aria-label="Card back">
  <div class="person">
    <h1 class="person__name">Dana R Holt</h1>
    <p class="person__title">Managing Director</p>
  </div>

  <ul class="contacts">
    <li><svg viewBox="0 0 16 16"><path d="M3 1h3l1.5 4-2 1.5a9 9 0 0 0 4 4L11 8.5l4 1.5v3a2 2 0 0 1-2 2A12 12 0 0 1 1 3a2 2 0 0 1 2-2z"/></svg>555-014-2290</li>
    <li><svg viewBox="0 0 16 16"><path d="M1 3h14v10H1z M1 3l7 6 7-6" stroke="#262626" stroke-width="1.2"/></svg>dana@ridgefieldag.com</li>
    <li><svg viewBox="0 0 16 16"><circle cx="8" cy="8" r="7"/><path d="M1 8h14M8 1c-3 3-3 11 0 14M8 1c3 3 3 11 0 14" stroke="#262626" stroke-width="1.1" fill="none"/></svg>www.ridgefieldag.com</li>
  </ul>

  <div class="brand">
    <span class="brand__dot"></span>
    <p class="brand__name">Ridgefield<small>Agriculture and Industry</small></p>
  </div>

  <p class="address">418 Cedar Row, Millbrook,<br>Fairview, US 560112</p>

  <svg class="bands" viewBox="0 0 680 70" aria-hidden="true">
    <rect x="0" y="28" width="330" height="42" fill="var(--grey)"/>
    <rect x="0" y="50" width="330" height="20" fill="var(--card)"/>
    <path d="M300 70 L300 28 Q300 16 316 16 L680 16 L680 70 Z" fill="var(--green)"/>
  </svg>
  <p class="tab-label">Ridgefield Agriculture and Industry</p>
</section>

</body>
</html>
```